Blind dating / hook up web

We're creating a new web application based on blind dates to hook up with others who like you (occasional dating, not long-term relationships): www.velvetquorra.com
The background idea is the same as other dating websites (there're many differences but probably don't matter for the design): to browse potential matching profiles based on several criteria (age, gender, zone, etc.) and vote for the ones you like (a yes/no answer just seeing the pictures and basic info, option to see the detailed profile including other users feedback about that profile). The other users do the same, and then, you can see the real matches and contact them.
The one who start the contact to matched profiles, should pay for it, discounting the cost from a previously funded credit balance.
There's also a section to browse for meeting places/plans suggestions.
After you had any date, you could leave feedback about the other, so, everyone had a reputation (similar to the Trandel's feedback system).
Of course, the other typical options: register/mail verification, profile edit, "loading..." stuff, etc.
We'll start with a typical website application, but we'll move to mobile app soon, so, a responsive design will be a plus.

We expect to get a design to use as a pattern to develop (our job) the application, so, we'll need to work with the winning designer to get the graphical pieces/elements (backgrounds, icons, sprites, etc.) not only the whole screen captures. We'll contact the finalists to discuss details about how much of this are included or not and possible future work if we need it.

We've got no previous work done on logos or color schemes, so, feel free to work on whatever you want.

Please, feel free to ask for details if you need more: plomworks@mivrano.net
Updates

One preference on our web development will be to use Bootstrap (or similar frameworks), so, if you know about it and you'd like to take in care, this will be a plus, not a must. If you think there will be something to gain on other design patterns, please, forget Bootstrap and put preference on the design itself.

After received the first drafts, I think there's something general to clarify:

Everybody seem to tend to include several romantic references... the website will not be dedicated to find a long term relationship but occasional affairs, so, maybe hearts aren't the best symbol and romantic pictures/slogans the best resources. 
Also we're searching for a different design/concept than other dating services... there're some key points to make it special (different from typical date websites): 
- Mark potential matching profiles with answering a simply Yes/No (I like / I don't like) 
- Blind dates: you finally don't know who are you going to meet, you just know both answered Yes. So, intrigue will be a better idea than love. 

Let’sfocus a little more what we have in mind to be a different dating site andwhat we expect to obtain with this design project:

The mainfunctionalities and, so, the most important parts to design are:

1. Viewinga sequence of potential matching profiles, answer a question similar to “do youwant to hook up he/she/them?” Clearly more “hot” than “sweet”… more erotic (notX) than love/tender… more prohibited/hidden/secret thanstandard/traditional/public/familiar…

This simplysystem can be the principal idea so, could take a good place in the home,before register showing the best rated profiles, and after register to show thepotential matches.

The sitewon’t be restricted to men/women, it will allow to register as couple too andthe mix of sexual orientations hetero/bi/homo... Of course you should registerand choose your filter parameters, but you’ll do it sometimes, not in everyvisit to the site.

The usershould see a big picture of each profile (this is the first attraction, we’rehooking up not searching for our whole-life partner) and just a few otherdetails like age and feedback rating from other users that already met thatprofile.

Thereshould be a way to review what profiles did you answer Yes and what No.

2. Anotherimportant part of the site is the one to create and propose meet plans. You canpost here your fantasies, your plans, your suggestions about what do you wantto do or what you propose for the meeting. This is where the search engine willtake place, to propose you places, ideas or services based on what you’refinding. This will be some kind of wizard or assistant, to “configure” yourideal meeting. It should suggest you activities to include in your plan and thesearch engine will suggest related places related to that activities. I.e.: ifI’d like to take a dinner, grab some beers and finish the night on a 5 starhotel suite, I’ll add “Dinner ideas”, “going out ideas” and “night stay ideas”(or something similar) and the engine will suggest me some near restaurants,pubs and hotels. Of course, you can enter your personalized plan manually inplain text or just select activities without taking any suggestion. (reserve aplace to suggest new activities to the system!)

Afterconfiguring your plan, you can post it to be realized some days and expose itto your matches to find anyone that like your plan.

This wizardwill allow you to browse the past plans to edit/reuse them and also receiveanswers from the matching profiles who like your plant to initiate the finalcontact and meet them.

3. Inanother section you should see plans posted by others and have the way toaccept or discard them.

4. Ofcourse, the homepage must not be as simple as the Yes/No answering section, it’simportant to explain what the service are and how it works, but, for us, it’smore important to see how the “daily” operative will show up than the home,because the home must be a reflect, a summary, of the operative surrounded bycatching slogans.

There’realso several related or secondary screens and resources to be designed, but,first, we’ll to focus on these four things. Drafts should reflect these ideasor will be very difficult to fit.

After revising a lot of designs sent, there's something we're doing wrong... maybe I'm not explaining myself well, so, let me try again to expose some important ideas and add some others that had appeared after a few designs that I thing they're on the right way:

- the site should be different from the "standard" dating services. Think more in casual meetings, sex encounters, swingers, hot nights, etc. Men, women or couples (even groups!) looking for anything... so, think on any kind of sexual orientation. People live in a stressed society, they're finding something different without loosing time... something spicy, intrigue, surprise, horny... just fun, not love, no sweet, no false promises... but at the same time, think on another way to structure it, another point of view, not the typical Register, browse, contact, meet.
- please, avoid the "register" form directly on the home... the user should take a full free tour all over the site without registering. The site will collect information about his/her/their preferences while he/she/they are looking what the site is about. When clicking on something that really need to be registered, then, the register form will appear already filled with all the collected information. Some kind of remember should appear if the user is using the site for a long time stuck, for example, answering yes/no to the profiles. But there shouldn't be any pressure to register, it should be a natural need after a while.
- The landing homepage should accomplish just three main objectives:
1. Explain what the service are about in just a few sentences (more about it later)
2. Choose your profile type preferences (I'm looking for...): men/women/couples, taking in care that I could find one, two or all three options... and enter to the site to see profiles
3. If I'm already registered, log in.
The login should be easy to see and find, but shouldn't be take too much importance.
The explaining sentences/section should be also easy to see, but can be a scroll down section
The most important and eye-catching should be the selector... with naughty pictures of men/women/couples to mark what you're looking for... maybe a title "What are you looking for?" and a site entrance "Let's hook-up!" that appears after choosing at least one option...
- After the landing homepage, the operational sections described on the previous update... where the backgrounds (and maybe the whole theme) should change according the user preferences... (don't show a women picture if the user isn't looking for women).
Don't think about if the design will end in a very difficult development! it's more important to have a good design and then, our developers will find the way to implement it. Don't be afraid of it! let your talent flow freely ;)

Many of your are using some kind of form to enter the search parameters... We want to try to avoid this and we're thinking on integrate the form on the homepage itself... something like to use icons to select "what I'm" (Man/Woman/Couple... in a similar way as many of you are showing the total profiles of each...); then, a second, bigger, selector to choose "what I'm looking for" (Men/Women/Couples, could select one or many)... maybe playing with big pictures or the background itself; finally (perhaps integrated with the results) some kind of slider to select the age range, leaving only the dropdowns to select the geographic location (if no one has a better idea with no typical "fields").

Industry/Entity Type

Dating

```html
<!DOCTYPE html>
<html lang="en">
<head>
<meta charset="utf-8">
<title>Velvet Quorra – Members</title>
<link href="https://fonts.googleapis.com/css2?family=Roboto+Slab:wght@300;400;700&family=Roboto:wght@400;700&family=Dancing+Script:wght@700&display=swap" rel="stylesheet">
<style>
  :root {
    --teal: #1f7f9e;
    --teal-dark: #16627c;
    --panel: rgba(26, 120, 152, 0.82);
    --panel-soft: rgba(120, 180, 200, 0.35);
    --pink: #e8286e;
    --pink-soft: #f07aa8;
    --white: #ffffff;
    --grey: #8f8f8f;
    --ink: #2b2b2b;
  }
  * { margin: 0; padding: 0; box-sizing: border-box; }
  html, body { width: 1200px; height: 653px; overflow: hidden; }
  body { position: relative; font-family: "Roboto", sans-serif; background: #777; }

  .backdrop {
    position: absolute; inset: 48px 0 0 0;
    background:
      radial-gradient(ellipse at 20% 70%, #5a5a5a 0%, transparent 45%),
      radial-gradient(ellipse at 85% 40%, #9a9a9a 0%, transparent 50%),
      linear-gradient(180deg, #8a8a8a 0%, #6d6d6d 55%, #8c8c8c 100%);
  }

  .topbar {
    position: absolute; top: 0; left: 0; width: 1200px; height: 48px;
    background: var(--white); border-bottom: 2px solid var(--teal);
  }
  .topbar .nav-link {
    position: absolute; top: 0; height: 46px; line-height: 52px;
    font-family: "Roboto Slab", serif; font-size: 10px; font-weight: 400;
    color: var(--teal-dark); letter-spacing: 0.3px; text-decoration: none;
  }
  .nav-link.active {
    background: linear-gradient(180deg, #f6a3c3 0%, #f07aa8 100%);
    color: var(--white); width: 68px; text-align: center;
  }
  .social {
    position: absolute; top: 18px; width: 15px; height: 15px;
    background: var(--teal-dark); border-radius: 1px;
  }

  .brand {
    position: absolute; left: 245px; top: 66px;
    font-family: "Roboto Slab", serif; font-weight: 300; font-size: 33px;
    color: var(--pink); letter-spacing: 0.5px;
  }
  .session { position: absolute; top: 62px; font-size: 7px; color: #ccc; }
  .session-btn {
    position: absolute; top: 62px; height: 11px; padding: 0 3px;
    border: 1px solid #ccc; border-radius: 2px;
    font-size: 6px; line-height: 9px; color: #eee;
  }

  .main-panel {
    position: absolute; left: 207px; top: 117px; width: 793px; height: 493px;
    background: var(--panel); border-radius: 3px;
  }

  .profile-card {
    position: absolute; left: 235px; top: 189px; width: 162px; height: 208px;
    background: var(--white); border-radius: 3px;
  }
  .profile-card .card-title {
    position: absolute; top: 11px; width: 100%; text-align: center;
    font-family: "Roboto Slab", serif; font-weight: 700; font-size: 10px; color: var(--pink);
  }
  .profile-photo {
    position: absolute; left: 20px; top: 36px; width: 124px; height: 122px;
    background: linear-gradient(160deg, #c9b7a6 0%, #8d7462 55%, #d9d0c8 100%);
  }
  .profile-info {
    position: absolute; left: 29px; top: 104px; font-family: "Roboto Slab", serif;
    font-size: 9.5px; line-height: 12px; color: var(--white);
  }
  .vote { position: absolute; top: 158px; height: 30px; width: 62px; }
  .vote.yes { left: 20px; background: var(--pink); }
  .vote.no { left: 83px; background: var(--grey); }
  .vote svg { position: absolute; left: 21px; top: 7px; }

  .feedback-box {
    position: absolute; left: 238px; top: 425px; width: 158px; height: 143px;
    background: var(--panel-soft);
  }
  .feedback-box p {
    position: absolute; left: 24px; top: 30px; width: 130px;
    font-weight: 700; font-size: 18.5px; line-height: 22px; color: var(--white);
  }

  .results-title {
    position: absolute; left: 444px; top: 139px; width: 474px; text-align: center;
    font-family: "Roboto Slab", serif; font-weight: 400; font-size: 25px; color: var(--white);
  }
  .results-sub {
    position: absolute; left: 444px; top: 174px; width: 618px; text-align: center;
    font-family: "Dancing Script", cursive; font-size: 24px; color: var(--pink); margin-left: -72px;
  }

  .result-row { position: absolute; left: 444px; width: 516px; height: 104px; }
  .tile { position: absolute; top: 0; height: 104px; }
  .tile span {
    position: absolute; left: 10px; bottom: 6px;
    font-family: "Roboto Slab", serif; font-weight: 700; font-size: 9px; color: var(--pink);
  }
  .tone-a { background: linear-gradient(170deg, #9b8d7c, #5f544a); }
  .tone-b { background: linear-gradient(160deg, #e6dcd3, #a38a78); }
  .tone-c { background: linear-gradient(180deg, #3d2e26, #8a6a58 60%, #3a2b24); }
  .tone-d { background: linear-gradient(160deg, #f3e3b8, #d4a86a); }

  .pager {
    position: absolute; left: 444px; top: 564px; width: 556px; text-align: center;
    font-family: "Dancing Script", cursive; font-size: 15px; color: var(--white); margin-left: -116px; padding-left: 150px;
  }
  .pager .current { color: var(--pink); }
</style>
</head>
<body>
  <div class="backdrop" role="img" aria-label="Black and white photograph of a person in a red swimsuit holding a shower rail under falling water"></div>

  <header class="topbar">
    <a class="nav-link" style="left:432px">HOME</a>
    <a class="nav-link" style="left:487px">MY MATCHES</a>
    <a class="nav-link active" style="left:571px">MEMBERS</a>
    <a class="nav-link" style="left:662px">LOCALS</a>
    <a class="nav-link" style="left:745px">CONTACT</a>
    <span class="social" style="left:810px"></span>
    <span class="social" style="left:837px"></span>
    <span class="social" style="left:862px"></span>
    <span class="social" style="left:889px"></span>
  </header>

  <div class="brand">VELVET QUORRA</div>
  <span class="session" style="left:772px">Hi, guest</span>
  <span class="session-btn" style="left:828px">SIGN IN</span>
  <span class="session-btn" style="left:865px">LOG OUT</span>

  <section class="main-panel"></section>

  <article class="profile-card">
    <div class="card-title">BACKY, 29</div>
    <div class="profile-photo" role="img" aria-label="Profile photo of Backy"></div>
    <div class="profile-info">BACKY<br>Age: 28<br>Wisconsin, United<br>States</div>
    <div class="vote yes"><svg width="20" height="16" viewBox="0 0 20 16"><path d="M2 8 L8 14 L18 2" stroke="#fff" stroke-width="4" fill="none"/></svg></div>
    <div class="vote no"><svg width="16" height="16" viewBox="0 0 16 16"><path d="M3 3 L13 13 M13 3 L3 13" stroke="#fff" stroke-width="3.5"/></svg></div>
  </article>

  <aside class="feedback-box"><p>TELL us your experience about VELVET QUORRA</p></aside>

  <h1 class="results-title">Hundred of people waiting for you</h1>
  <h2 class="results-sub">Search results</h2>

  <div class="result-row" style="top:225px">
    <div class="tile tone-a" style="left:0;width:111px" role="img" aria-label="Profile photo of Backy"><span>BACKY, 29</span></div>
    <div class="tile tone-b" style="left:112px;width:139px" role="img" aria-label="Profile photo of Jessica"><span>JESSICA, 29</span></div>
    <div class="tile tone-c" style="left:252px;width:152px" role="img" aria-label="Profile photo of Amy"><span>AMY, 20</span></div>
    <div class="tile tone-a" style="left:405px;width:111px" role="img" aria-label="Profile photo of Lana"><span>LANA, 19</span></div>
  </div>
  <div class="result-row" style="top:336px">
    <div class="tile tone-d" style="left:0;width:138px" role="img" aria-label="Profile photo of Backy"><span>BACKY, 29</span></div>
    <div class="tile tone-c" style="left:139px;width:126px" role="img" aria-label="Profile photo of Jessica"><span>JESSICA, 29</span></div>
    <div class="tile tone-a" style="left:266px;width:110px" role="img" aria-label="Profile photo of Amy"><span>AMY, 20</span></div>
    <div class="tile tone-b" style="left:377px;width:139px" role="img" aria-label="Profile photo of Lana"><span>LANA, 19</span></div>
  </div>
  <div class="result-row" style="top:445px">
    <div class="tile tone-a" style="left:0;width:111px" role="img" aria-label="Profile photo of Backy"><span>BACKY, 29</span></div>
    <div class="tile tone-b" style="left:112px;width:139px" role="img" aria-label="Profile photo of Jessica"><span>JESSICA, 29</span></div>
    <div class="tile tone-c" style="left:252px;width:152px" role="img" aria-label="Profile photo of Amy"><span>AMY, 20</span></div>
    <div class="tile tone-a" style="left:405px;width:111px" role="img" aria-label="Profile photo of Lana"><span>LANA, 19</span></div>
  </div>

  <nav class="pager"><span class="current">1</span> 2 3 4 5 6 7 ... next page</nav>
</body>
</html>
```